Electrical & Communications Company Wordpress Themed Website Design

Hi everyone,

I need a wordpress themed website designed for a new company based in Sydney Australia called "VELTRIX". It delivers electrical and communication services to the domestic and commercial sectors.

It needs to be the FULL/COMPLETE wordpress theme! A clean and easy to use site.

Please guys take the time to look at these competitors sites:

www.tapnovo.com.au
www.harbelwiring.com.au
www.qul.com.au
www.lumavoltics.com.au
www.corbinwiring.com.au
www.fendrasparkies.com.au

Please use these site for ideas only!!! we want to be original.

(If you would like to add electrical and communications to the logo that is O.K.)

Note: These logo's are registered trademarks of veltrix pty ltd.

Accreditation:

Ubta member (Federated wiring and signalling guild)

PLEASE CHECK THE WEB PLANNING LAYOUT BELOW FOR ROUGH IDEA
Updates

Have requested to increase payment to $400 and now guarantee payment!

Hi guys, forgot to mention i would like to see the business phone number prominently some where with a call to action.As we are a service business and need people to easly be able to see our contact number. Maybe top right courner but open to ideas. 

 Guys/Girls this is for a complete working word press theme that i can load up on the sever and access thru wordpress admin. Code etc

Industry/Entity Type

Communications

Requirements
Must have
• - Logo Provided must be used
• - Themes and colours to be consisted with with brand
• - Fully customizable
• - Have a social share button from shariq.com
• - Must be the full/complete theme for word press
Nice to have
• - pixtorvault
• - contactform
• - would like zenda orbit pay quidlo displayed
• - Guarantee logo or something
Should not have
• - Please don't waste your or our time submitting templates or copies of other sites original only!

```html
<!DOCTYPE html>
<html lang="en">
<head>
<meta charset="utf-8">
<title>VELTRIX – Electrical &amp; Communications</title>
<link href="https://fonts.googleapis.com/css2?family=Noto+Sans:wght@400;700&display=swap" rel="stylesheet">
<style>
:root{
  --red:#e0151e;
  --red-dark:#b10c13;
  --charcoal:#4b4c4e;
  --ink:#222;
  --grey:#555;
  --muted:#888;
  --line:#d8d8d8;
  --panel:#fff;
  --bg-top:#e3151d;
  --bg-bottom:#232323;
}
*{box-sizing:border-box;margin:0;padding:0}
html,body{width:1097px;height:1200px;overflow:hidden}
body{
  font-family:"Noto Sans",sans-serif;color:var(--ink);position:relative;
  background:linear-gradient(180deg,var(--bg-top) 0,#c8141b 180px,#5a1214 420px,var(--bg-bottom) 620px,var(--bg-bottom) 100%);
}
.abs{position:absolute}
.page{left:130px;top:14px;width:837px;height:1158px;background:var(--panel);border-radius:16px;
  background:linear-gradient(180deg,#eee 0,#fff 60px,#fff 100%)}
/* header */
.logo{left:147px;top:46px;display:flex;align-items:center;gap:8px}
.logo-dot{width:30px;height:30px;border-radius:50%;background:var(--red)}
.logo-name{font-size:38px;font-weight:700;color:var(--red);letter-spacing:-1px}
.call-icon{left:523px;top:49px;width:33px;height:33px;border-radius:6px;background:var(--red);display:flex;align-items:center;justify-content:center}
.call-divider{left:563px;top:48px;width:1px;height:40px;background:var(--line)}
.call-label{left:573px;top:46px;font-size:13px;font-weight:700;color:var(--charcoal)}
.call-number{left:573px;top:58px;font-size:25px;font-weight:700;color:var(--charcoal);letter-spacing:.5px}
.follow{left:790px;top:45px;font-size:9px;font-weight:700;color:var(--charcoal)}
.socials{left:788px;top:62px;display:flex;gap:6px}
.social{display:flex;flex-direction:column;align-items:center;gap:2px;font-size:8px;color:var(--charcoal);width:30px}
.social span.sq{width:22px;height:22px;border-radius:4px;background:var(--charcoal)}
/* nav */
.nav{left:146px;top:122px;width:805px;height:34px;border-radius:6px;border:1px solid #ccc;
  background:linear-gradient(180deg,#fafafa,#d9d9d9 48%,#cfcfcf 52%,#ececec);display:flex;align-items:center;padding-left:16px}
.nav a{font-size:11px;font-weight:700;color:var(--charcoal);text-decoration:none;padding:0 32px;line-height:30px;border-right:1px solid #bbb;height:14px;display:flex;align-items:center}
.nav a:last-child{border:0}
.nav a.active{background:var(--charcoal);color:#fff;height:31px;padding:0 22px}
/* hero */
.hero{left:147px;top:169px;width:804px;height:236px;border-radius:8px;background:linear-gradient(180deg,#ef2029,var(--red-dark));border:1px solid #ccc}
.hero-photo{left:152px;top:174px;width:582px;height:226px;border-radius:4px 140px 140px 4px / 4px 226px 226px 4px;
  background:linear-gradient(135deg,#1f3550 0,#4e7aa8 35%,#9cc4e6 70%,#dfeaf3 100%)}
.perk{left:757px;width:184px;height:65px;border-radius:8px;background:linear-gradient(180deg,#fff,#e6e6e6);
  display:flex;flex-direction:column;align-items:center;justify-content:center;color:var(--charcoal);font-weight:700;font-size:16px;line-height:1.1;text-align:center}
.perk small{font-size:13px}
/* content */
.welcome-title{left:147px;top:428px;font-size:16px;color:var(--red)}
.welcome-text{left:147px;top:457px;width:555px;font-size:10.5px;line-height:12px;color:var(--ink)}
.sector{width:175px;height:115px;border-radius:6px;background:var(--charcoal);border:2px solid #3a3b3d;overflow:hidden}
.sector-img{height:87px}
.sector-label{display:flex;justify-content:space-between;align-items:center;padding:0 8px;height:24px;font-size:8.5px;letter-spacing:.5px;color:#fff}
.sector-label b{color:var(--red);font-size:11px}
.pride{left:147px;top:660px;width:560px;font-size:10.5px;line-height:13px}
.services-title{left:147px;top:702px;font-size:11px;font-weight:700}
.services{left:147px;top:731px;width:564px;height:110px;border-radius:8px;background:var(--charcoal)}
.svc{font-size:11px;color:#fff;display:flex;align-items:center;gap:6px}
.svc::before{content:"";width:5px;height:8px;background:var(--red);clip-path:polygon(0 0,100% 50%,0 100%)}
/* testimonial */
.box{border:1px solid var(--line);border-radius:8px;background:#fff}
.red-head{height:33px;border-radius:7px 7px 0 0;background:linear-gradient(180deg,#ee2029,var(--red-dark));color:#fff;font-size:16px;padding:6px 16px}
.portrait{left:157px;top:894px;width:108px;height:124px;border:1px solid #ccc;background:linear-gradient(180deg,#d9dde2,#7c8087 60%,#2b2d31)}
.t-name{left:277px;top:898px;font-size:11px;font-weight:700;color:var(--grey);line-height:17px}
.t-quote{left:277px;top:935px;width:180px;font-size:9px;line-height:11.5px;color:var(--grey)}
.t-rating{left:277px;top:997px;font-size:11px;font-weight:700;color:var(--grey);display:flex;gap:4px;align-items:center}
.offer-title{left:481px;top:870px;width:230px;text-align:center;color:var(--red);font-weight:700;line-height:1}
.offer-title .a{font-size:21px;font-style:italic}
.offer-title .b{font-size:17px}
.offer-number{left:481px;top:907px;width:230px;text-align:center;font-size:24px;font-weight:700;color:var(--grey)}
.offer-rule{left:481px;top:952px;width:230px;height:1px;background:#eee}
.cards{left:505px;top:965px;width:190px;display:flex;flex-wrap:wrap;gap:6px 10px}
.cards span{font-size:10px;font-weight:700;color:var(--charcoal)}
/* sidebar */
.form-label{font-size:9.5px;color:var(--ink)}
.field{width:156px;height:19px;border:1px solid #bbb;border-radius:4px;background:linear-gradient(180deg,#eee,#fff)}
.btn{height:19px;width:59px;border:1px solid #aaa;border-radius:4px;background:linear-gradient(180deg,#fff,#d4d4d4);font-size:10px;display:flex;align-items:center;justify-content:center;color:var(--ink)}
.search{left:751px;top:753px;width:155px;height:19px;border:1px solid #bbb;border-radius:4px 0 0 4px;font-size:9px;padding:3px 8px}
.go{left:906px;top:753px;width:24px;height:19px;border:1px solid #aaa;border-radius:0 4px 4px 0;background:linear-gradient(180deg,#fff,#cfcfcf);font-size:9px;font-weight:700;display:flex;align-items:center;justify-content:center}
.post{left:748px;display:flex;gap:8px}
.thumb{width:43px;height:40px;border:1px solid #ccc;background:linear-gradient(180deg,#f4f4f4,#d6d6d6)}
.post h4{font-size:9.5px;font-weight:700;margin-top:2px}
.post p{font-size:9.5px;line-height:11px;color:var(--ink)}
.post-rule{left:733px;width:216px;height:1px;background:#eee}
.cta{left:147px;top:1040px;width:803px;height:39px;border-radius:7px;background:linear-gradient(180deg,#ee2029,var(--red-dark));
  color:#fff;font-size:18px;font-weight:700;display:flex;align-items:center;justify-content:center}
.footer-rule{left:130px;top:1091px;width:837px;height:1px;background:#e6e6e6}
.footer-links{left:130px;top:1114px;width:837px;text-align:center;font-size:10px;color:var(--muted)}
.copy{left:130px;top:1132px;width:837px;text-align:center;font-size:10px;color:var(--muted)}
</style>
</head>
<body>
<div class="abs page"></div>

<header>
  <div class="abs logo"><span class="logo-dot"></span><span class="logo-name">VELTRIX</span></div>
  <div class="abs call-icon">
    <svg width="20" height="20" viewBox="0 0 24 24"><path fill="#fff" d="M6.6 10.8a15.1 15.1 0 0 0 6.6 6.6l2.2-2.2c.3-.3.7-.4 1-.2 1.1.4 2.3.6 3.6.6.6 0 1 .4 1 1V20c0 .6-.4 1-1 1C10.6 21 3 13.4 3 4c0-.6.4-1 1-1h3.5c.6 0 1 .4 1 1 0 1.3.2 2.5.6 3.6.1.3 0 .7-.2 1l-2.3 2.2z"/></svg>
  </div>
  <div class="abs call-divider"></div>
  <div class="abs call-label">CALL US TODAY!</div>
  <div class="abs call-number">02 5550 1827</div>
  <div class="abs follow">Follow us on:</div>
  <div class="abs socials">
    <div class="social"><span class="sq"></span>Chirply</div>
    <div class="social"><span class="sq"></span>Folkbook</div>
    <div class="social"><span class="sq"></span>Linkora</div>
    <div class="social"><span class="sq"></span>Feed</div>
  </div>
</header>

<nav class="abs nav">
  <a class="active">Home</a><a>Our Services</a><a>Quotes</a><a>Links</a><a>Contact us</a>
</nav>

<section>
  <div class="abs hero"></div>
  <div class="abs hero-photo" role="img" aria-label="Photo looking up at glass office towers against a blue sky"></div>
  <div class="abs perk" style="top:177px">24hours<small>7 days a week</small></div>
  <div class="abs perk" style="top:255px">No Callout Fee</div>
  <div class="abs perk" style="top:331px">Fixed Pricing</div>
</section>

<main>
  <h1 class="abs welcome-title" style="font-weight:400">Welcome</h1>
  <p class="abs welcome-text"><b>VELTRIX</b> is a new and rapidly expanding Electrical &amp; Communications Company that services the Domestic, Commercial &amp; Industrial sectors. Our service ranges from minor refurbishments to major installations, we also have a well maintained and efficient service team providing on-going support for all of your maintenance needs.</p>

  <div class="abs sector" style="left:147px;top:524px"><div class="sector-img" role="img" aria-label="Photo of a suburban family house" style="background:linear-gradient(180deg,#3f7bd0,#9cc0ea 55%,#c9c6b8 75%,#6f8a4e)"></div><div class="sector-label">DOMESTIC<b>›</b></div></div>
  <div class="abs sector" style="left:342px;top:524px"><div class="sector-img" role="img" aria-label="Photo of city office buildings lit at night" style="background:linear-gradient(180deg,#0d1a2c,#2a4a5e 55%,#7a8d5e 80%,#1c2a36)"></div><div class="sector-label">COMMERCIAL<b>›</b></div></div>
  <div class="abs sector" style="left:537px;top:524px"><div class="sector-img" role="img" aria-label="Photo of an industrial plant lit at dusk" style="background:linear-gradient(180deg,#1f4d9a,#3c6fb8 45%,#c9923a 75%,#5a3a1a)"></div><div class="sector-label">INDUSTRIAL<b>›</b></div></div>

  <p class="abs pride">We pride ourselves on our commitment to professionalism and our great attention to detail. We are gning a reputation with our customers for our quality workmanship, friendly attitude &amp; reliable service.</p>
  <h2 class="abs services-title">OUR SERVICES:</h2>
  <div class="abs services"></div>
  <div class="abs svc" style="left:163px;top:747px">Air Conditioning</div>
  <div class="abs svc" style="left:163px;top:768px">Lighting</div>
  <div class="abs svc" style="left:163px;top:788px">Hot Water systems</div>
  <div class="abs svc" style="left:163px;top:809px">Power Outlets</div>
  <div class="abs svc" style="left:309px;top:747px">Electrical Services</div>
  <div class="abs svc" style="left:309px;top:768px">Commercial Electrician</div>
  <div class="abs svc" style="left:309px;top:788px">Test &amp; Tag</div>
  <div class="abs svc" style="left:309px;top:809px">Phone &amp; data networking</div>
  <div class="abs svc" style="left:491px;top:747px">Transformer/Switchboard Upgrades</div>
  <div class="abs svc" style="left:491px;top:768px">Surge Protection</div>
  <div class="abs svc" style="left:491px;top:788px">Commercial Electrical</div>

  <div class="abs box" style="left:147px;top:852px;width:323px;height:177px"><div class="red-head">Testimonial</div></div>
  <div class="abs portrait" role="img" aria-label="Portrait photo of a client"></div>
  <div class="abs t-name">Name<br>Designation</div>
  <p class="abs t-quote">We pride ourselves on our commit-ment to professionalism and our great attention to detail. We are gning a reputation with our custom-ers for our quality.</p>
  <div class="abs t-rating">Rating
    <svg width="92" height="15" viewBox="0 0 92 15" fill="#e0151e">
      <g id="st"><path d="M7.5 0l2.2 4.9 5.3.5-4 3.6 1.2 5.2-4.7-2.8-4.7 2.8 1.2-5.2-4-3.6 5.3-.5z"/></g>
      <use href="#st" x="18"/><use href="#st" x="36"/><use href="#st" x="54"/><use href="#st" x="72"/>
    </svg>
  </div>

  <div class="abs box" style="left:481px;top:852px;width:230px;height:177px"></div>
  <div class="abs offer-title"><div class="a">Special Offers</div><div class="b">Call Now!</div></div>
  <div class="abs offer-number">02 5550 1827</div>
  <div class="abs offer-rule"></div>
  <div class="abs cards"><span>ZENDA</span><span>ZENDA FLOW</span><span>PIVOTA</span><span>ORBIT PAY</span><span style="font-size:13px">quidlo</span></div>
</main>

<aside>
  <div class="abs box" style="left:732px;top:424px;width:218px;height:296px"></div>
  <div class="abs form-label" style="left:765px;top:443px">Name:</div>
  <div class="abs field" style="left:765px;top:458px"></div>
  <div class="abs form-label" style="left:765px;top:486px">Email:</div>
  <div class="abs field" style="left:765px;top:501px"></div>
  <div class="abs form-label" style="left:765px;top:530px">Subject:</div>
  <div class="abs field" style="left:765px;top:545px"></div>
  <div class="abs form-label" style="left:765px;top:573px">Message:</div>
  <div class="abs field" style="left:765px;top:588px;height:79px"></div>
  <div class="abs btn" style="left:765px;top:679px">Send</div>
  <div class="abs btn" style="left:861px;top:679px">Clear</div>

  <div class="abs box" style="left:732px;top:731px;width:218px;height:62px"></div>
  <div class="abs search">Search...</div>
  <div class="abs go">GO</div>

  <div class="abs box" style="left:732px;top:804px;width:218px;height:225px"><div class="red-head">Latest Blog posts</div></div>
  <div class="abs post" style="top:854px"><div class="thumb" role="img" aria-label="Post author avatar"></div><div><h4>Heading goes here!</h4><p>Text goes here...<br>Text goes here...</p></div></div>
  <div class="abs post-rule" style="top:903px"></div>
  <div class="abs post" style="top:912px"><div class="thumb" role="img" aria-label="Post author avatar"></div><div><h4>Heading goes here!</h4><p>Text goes here...<br>Text goes here...</p></div></div>
  <div class="abs post-rule" style="top:960px"></div>
  <div class="abs post" style="top:969px"><div class="thumb" role="img" aria-label="Post author avatar"></div><div><h4>Heading goes here!</h4><p>Text goes here...<br>Text goes here...</p></div></div>
</aside>

<div class="abs cta">Call Us Today For A No Obligation Quote</div>

<footer>
  <div class="abs footer-rule"></div>
  <div class="abs footer-links">Home | &nbsp;Our Services | &nbsp;Quotes | &nbsp;Links &nbsp;| &nbsp;Contact us</div>
  <div class="abs copy">© 2010 veltrix</div>
</footer>
</body>
</html>
```